Graphic design for "How It Works" for VelmoraStyles.com*

VelmoraStyles.com website is for selling custom designer outfits for women and girls in all countries, customers can choose existing designs on this website and customize to their measurements. Customers can also provide their own designs and measurements and our expert designers and tailors get the outfit stitched and delivered to the customer.

We wanted to explain how this entire process works in 4 steps in the form of graphic design with little heading and text describing each step.

Step 1: Select Dress
Its time to choose the beauty you want to adorn yourself with. We have a wide collection of premium dresses, colours and accessories. There is something for everyone! All you need to do is pick. If you can’t find what you are looking for then you can share a picture of what you want, we will get it done whatever you want.

Step 2: Customization
Everyone is different; hence we realise the need for customization of the design and size. Here you select exactly how you want your dress to be. From sleeves to cuts, everything will be done as per your wish. Enter your measurements, lo and behold! You’re done. Leave your comments for even more customization.

Step 3: Designer Consultation
We as a user-friendly brand, aspire to provide the best of services to our clients. Our expert lady designers will help you for everything right from selecting of fabric to design of dress to necessary accessories. Our designers are just a call away!

Step 4: Stitch and Deliver
After you have placed your order, we confirm and verify the details. The boutique completes your order, sends it to us and we deliver it to your doorstep. We also have a team of designers in-house to cater to your premium dressing needs.

```html
<!DOCTYPE html>
<html lang="en">
<head>
<meta charset="utf-8">
<title>How It Works – VelmoraStyles.com</title>
<link href="https://fonts.googleapis.com/css2?family=Montserrat:wght@900&family=Roboto+Condensed:wght@600;700&family=PT+Sans:wght@400;700&display=swap" rel="stylesheet">
<style>
  :root {
    --backdrop: #f2b5b5;
    --paper: #ffffff;
    --ink: #111111;
    --magenta: #c8548a;
    --violet: #5752a8;
    --cyan: #1d9fc6;
    --teal: #19c08f;
    --lime: #76d41e;
    --ring: #ececec;
  }
  * { margin: 0; padding: 0; box-sizing: border-box; }
  html, body { width: 1196px; height: 1200px; overflow: hidden; background: var(--backdrop); }
  .poster {
    position: absolute; left: 188px; top: 20px;
    width: 733px; height: 1037px;
    background: var(--paper);
    transform: scale(1.119); transform-origin: top left;
    overflow: hidden;
  }
  .poster-art { position: absolute; inset: 0; }
  .title {
    position: absolute; top: 32px; left: 0; width: 100%;
    text-align: center;
    font: 900 44px/52px "Montserrat", sans-serif;
    color: var(--ink); letter-spacing: 0.5px;
  }
  .step { position: absolute; width: 175px; }
  .step-label {
    font-family: "Roboto Condensed", sans-serif; font-weight: 700;
    color: var(--ink); font-size: 14px; line-height: 1;
    display: flex; align-items: baseline; gap: 6px; margin-bottom: 8px;
  }
  .step-number { color: var(--magenta); font-size: 38px; }
  .step-text {
    font: 400 10.6px/14.2px "PT Sans", sans-serif; color: var(--ink);
  }
  .step-1 { left: 111px; top: 124px; }
  .step-2 { left: 450px; top: 320px; }
  .step-3 { left: 111px; top: 524px; width: 170px; }
  .step-4 { left: 450px; top: 720px; }
  .band-label {
    font: 700 14px "Roboto Condensed", sans-serif; fill: #fff; letter-spacing: 0.3px;
  }
  .website {
    position: absolute; left: 0; width: 100%; top: 995px;
    text-align: center; font: 400 25px/30px "PT Sans", sans-serif; color: #fff;
  }
</style>
</head>
<body>
<main class="poster">
  <svg class="poster-art" viewBox="0 0 733 1037" width="733" height="1037" aria-hidden="false">
    <defs>
      <linearGradient id="arc-blue-green" x1="0" y1="0" x2="0" y2="1">
        <stop offset="0" stop-color="#1d9fc6"/><stop offset="1" stop-color="#19c08f"/>
      </linearGradient>
      <linearGradient id="arc-teal-green" x1="0" y1="0" x2="0" y2="1">
        <stop offset="0" stop-color="#1cc4a0"/><stop offset="1" stop-color="#19c08f"/>
      </linearGradient>
      <linearGradient id="arc-green-lime" x1="0" y1="0" x2="0" y2="1">
        <stop offset="0" stop-color="#19c08f"/><stop offset="1" stop-color="#8bd12a"/>
      </linearGradient>
      <linearGradient id="arc-lime-yellow" x1="0" y1="0" x2="0" y2="1">
        <stop offset="0" stop-color="#76d41e"/><stop offset="1" stop-color="#f2c200"/>
      </linearGradient>
      <radialGradient id="scene-fill" cx="0.5" cy="0.5" r="0.5">
        <stop offset="0" stop-color="#e3e2f7"/><stop offset="1" stop-color="#f7f5fb"/>
      </radialGradient>
      <path id="path-select" d="M351,130 A188,188 0 0 0 351,330"/>
      <path id="path-custom" d="M353,328 A188,188 0 0 1 353,528"/>
      <path id="path-consult" d="M351,526 A188,188 0 0 0 351,726"/>
      <path id="path-stitch" d="M353,724 A188,188 0 0 1 353,924"/>
    </defs>

    <!-- title rules -->
    <line x1="71" y1="58" x2="158" y2="58" stroke="var(--magenta)" stroke-width="3"/>
    <line x1="576" y1="58" x2="662" y2="58" stroke="var(--magenta)" stroke-width="3"/>

    <!-- step timeline bands -->
    <g class="timeline" fill="none" stroke-width="46">
      <use href="#path-select" stroke="var(--violet)"/>
      <use href="#path-custom" stroke="var(--cyan)"/>
      <use href="#path-consult" stroke="var(--teal)"/>
      <use href="#path-stitch" stroke="var(--lime)"/>
    </g>
    <text class="band-label" dominant-baseline="middle"><textPath href="#path-select" startOffset="50%" text-anchor="middle">SELECT DRESS</textPath></text>
    <text class="band-label" dominant-baseline="middle"><textPath href="#path-custom" startOffset="50%" text-anchor="middle">CUSTOMIZATION</textPath></text>
    <text class="band-label" dominant-baseline="middle"><textPath href="#path-consult" startOffset="50%" text-anchor="middle">DESIGNER CONSULTATION</textPath></text>
    <text class="band-label" dominant-baseline="middle"><textPath href="#path-stitch" startOffset="50%" text-anchor="middle">STITCH AND DELIVER</textPath></text>

    <!-- step badges -->
    <g class="badge badge-1">
      <path d="M497,157 A82,82 0 1 0 497,299" fill="none" stroke="url(#arc-blue-green)" stroke-width="6" stroke-linecap="round"/>
      <circle cx="456" cy="228" r="64" fill="#fff" stroke="var(--ring)" stroke-width="12"/>
      <circle cx="456" cy="228" r="56" fill="url(#scene-fill)" role="img" aria-label="Illustration of a dress shown in an online catalogue"/>
    </g>
    <g class="badge badge-2">
      <path d="M219,354 A82,82 0 1 1 219,496" fill="none" stroke="url(#arc-teal-green)" stroke-width="6" stroke-linecap="round"/>
      <circle cx="260" cy="425" r="64" fill="#fff" stroke="var(--ring)" stroke-width="12"/>
      <circle cx="260" cy="425" r="56" fill="url(#scene-fill)" role="img" aria-label="Illustration of a shopper customising a dress on a screen"/>
    </g>
    <g class="badge badge-3">
      <path d="M497,552 A82,82 0 1 0 497,694" fill="none" stroke="url(#arc-green-lime)" stroke-width="6" stroke-linecap="round"/>
      <circle cx="456" cy="623" r="64" fill="#fff" stroke="var(--ring)" stroke-width="12"/>
      <circle cx="456" cy="623" r="56" fill="url(#scene-fill)" role="img" aria-label="Illustration of designers consulting beside a dress board"/>
    </g>
    <g class="badge badge-4">
      <path d="M219,759 A82,82 0 1 1 219,901" fill="none" stroke="url(#arc-lime-yellow)" stroke-width="6" stroke-linecap="round"/>
      <circle cx="260" cy="830" r="64" fill="#fff" stroke="var(--ring)" stroke-width="12"/>
      <circle cx="260" cy="830" r="56" fill="url(#scene-fill)" role="img" aria-label="Illustration of tailoring and a parcel being delivered to a customer"/>
    </g>

    <!-- footer wave -->
    <path d="M0,890 Q330,1010 733,826 L733,1037 L0,1037 Z" fill="var(--magenta)"/>
    <path d="M0,912 Q340,1012 733,842" fill="none" stroke="#1a1a1a" stroke-width="2"/>
  </svg>

  <h1 class="title">HOW IT WORKS</h1>

  <section class="step step-1">
    <h2 class="step-label">STEP <span class="step-number">01</span></h2>
    <p class="step-text">Its time to choose the beauty you want to adorn yourself with. We have a wide collection of premium dresses, colours and accessories. There is something for everyone! All you need to do is pick. If you can’t find what you are looking for then you can share a picture of what you want, we will get it done whatever you want.</p>
  </section>

  <section class="step step-2">
    <h2 class="step-label">STEP <span class="step-number">02</span></h2>
    <p class="step-text">Everyone is different; hence we realise the need for customization of the design and size. Here you select exactly how you want your dress to be. From sleeves to cuts, everything will be done as per your wish. Enter your measurements, lo and behold! You’re done. Leave your comments for even more customization.</p>
  </section>

  <section class="step step-3">
    <h2 class="step-label">STEP <span class="step-number">03</span></h2>
    <p class="step-text">We as a user-friendly brand, aspire to provide the best of services to our clients. Our expert lady designers will help you for everything right from selecting of fabric to design of dress to necessary accessories. Our designers are just a call away!</p>
  </section>

  <section class="step step-4">
    <h2 class="step-label">STEP <span class="step-number">04</span></h2>
    <p class="step-text">After you have placed your order, we confirm and verify the details. The boutique completes your order, sends it to us and we deliver it to your doorstep. We also have a team of designers in-house to cater to your premium dressing needs.</p>
  </section>

  <p class="website">www.velmorastyles.com</p>
</main>
</body>
</html>
```